Vantor Advisory business card

Premium business card required
I have attached the brand as a powerpoint template but this can be made to look very up market, I have also attached my BIO for title reasons and to give you a feel for my skills
front of card
Derek Holloway
Managing Director Vantor Advisory
Retail, Customer-Led Experience, Transformation and Maximising Shareholder Return
Mobile +61(0)418557392
Email derekvantoradvisory.com
back of card

VANTOR ADVISORY’ OFFERING

We transform customer environments to extract benefits while elevating service levels;
We release millions of dollars in self-funding through continuous improvement;
We see CX as a key differentiator, proactively guarding share from market disrupters;
We re-invent service and create front-end of the future.

```html
<!DOCTYPE html>
<html lang="en">
<head>
<meta charset="utf-8">
<title>Vantor Advisory business card</title>
<link rel="stylesheet" href="https://fonts.googleapis.com/css2?family=Open+Sans:wght@400;600;700&display=swap">
<style>
  :root {
    --backdrop: #3b3531;
    --card: #0d0d0d;
    --gold: #e6c01e;
    --silver: #c4c4c4;
    --ink: #e4e4e4;
  }
  * { margin: 0; padding: 0; box-sizing: border-box; }
  html, body { width: 1200px; height: 900px; overflow: hidden; }
  body {
    background: var(--backdrop);
    font-family: "Open Sans", Arial, sans-serif;
    position: relative;
  }
  .card {
    position: absolute;
    width: 540px;
    height: 310px;
    background: var(--card);
    border-radius: 3px;
    box-shadow: 0 12px 30px rgba(0,0,0,.45);
  }
  .card--front { left: 30px; top: 300px; }
  .card--back  { left: 630px; top: 300px; }

  .brand {
    position: absolute;
    display: flex;
    align-items: center;
    gap: 12px;
  }
  .brand__dot {
    width: 34px; height: 34px;
    border-radius: 50%;
    background: var(--silver);
    flex: none;
  }
  .brand__name {
    font-weight: 600;
    font-size: 24px;
    letter-spacing: .5px;
    color: var(--silver);
    white-space: nowrap;
  }
  .card--front .brand { left: 210px; top: 56px; }
  .card--back .brand { left: 50%; top: 50%; transform: translate(-50%, -50%); }
  .card--back .brand__name { font-size: 28px; }
  .card--back .brand__dot { width: 40px; height: 40px; }

  .contact {
    position: absolute;
    left: 34px;
    bottom: 32px;
    color: var(--ink);
    font-size: 13.5px;
    line-height: 1.45;
  }
  .contact__name {
    color: var(--gold);
    font-weight: 700;
    font-size: 19px;
    letter-spacing: .4px;
    text-transform: uppercase;
    margin-bottom: 2px;
  }
  .contact__role { max-width: 380px; }
  .contact__lines { margin-top: 14px; list-style: none; }
  .contact__lines li { display: flex; align-items: center; gap: 9px; }
  .contact__icon { width: 12px; height: 12px; flex: none; }
</style>
</head>
<body>
  <section class="card card--front" aria-label="Card front">
    <div class="brand">
      <span class="brand__dot"></span>
      <span class="brand__name">VANTOR ADVISORY</span>
    </div>
    <div class="contact">
      <p class="contact__name">Derek Holloway</p>
      <p class="contact__role">Managing Director Vantor Advisory<br>Retail, Customer-Led Experience, Transformation and Maximising Shareholder Return</p>
      <ul class="contact__lines">
        <li>
          <svg class="contact__icon" viewBox="0 0 24 24" aria-hidden="true"><path fill="#e6c01e" d="M6.6 10.8a15.1 15.1 0 0 0 6.6 6.6l2.2-2.2c.3-.3.7-.4 1-.2 1.1.4 2.3.6 3.6.6.6 0 1 .4 1 1V20c0 .6-.4 1-1 1A17 17 0 0 1 3 4c0-.6.4-1 1-1h3.5c.6 0 1 .4 1 1 0 1.3.2 2.5.6 3.6.1.3 0 .7-.2 1z"/></svg>
          <span>+61(0)418557392</span>
        </li>
        <li>
          <svg class="contact__icon" viewBox="0 0 24 24" aria-hidden="true"><rect x="2" y="5" width="20" height="14" rx="1" fill="#e6c01e"/><path d="M2.5 5.5 12 13l9.5-7.5" fill="none" stroke="#0d0d0d" stroke-width="1.6"/></svg>
          <span>derekvantoradvisory.com</span>
        </li>
      </ul>
    </div>
  </section>

  <section class="card card--back" aria-label="Card back">
    <div class="brand">
      <span class="brand__dot"></span>
      <span class="brand__name">VANTOR ADVISORY</span>
    </div>
  </section>
</body>
</html>
```